Ferndale Chapel of Grace (this will be used for new church sign) sign will be 4'x8' and would like also listed Sunday School 9:00am Worship Service 10:30am.

Logo Text

FERNDALE CHAPEL OF GRACE

```html
<!DOCTYPE html>
<html lang="en">
<head>
<meta charset="utf-8">
<title>Ferndale Chapel of Grace – Church Sign</title>
<link href="https://fonts.googleapis.com/css2?family=Poppins:wght@400;500;600;700;800&display=swap" rel="stylesheet">
<style>
  :root {
    --crimson: #bd1a45;
    --crimson-deep: #a10f2e;
    --gold: #c9a800;
    --ink: #1c1c1c;
    --black: #000000;
    --white: #ffffff;
    --page: #e0e0e0;
  }
  * { margin: 0; padding: 0; box-sizing: border-box; }
  html, body {
    width: 1200px; height: 1200px; overflow: hidden;
    background: var(--page);
    font-family: "Poppins", sans-serif;
  }
  .sign {
    position: absolute; left: 63px; top: 332px;
    width: 1073px; height: 536px;
    background: var(--white);
    overflow: hidden;
  }
  .brand {
    position: absolute; left: 168px; top: 62px;
    display: flex; align-items: center; gap: 10px;
  }
  .brand-mark {
    width: 26px; height: 26px; border-radius: 50%;
    background: var(--gold);
  }
  .brand-name {
    color: var(--crimson); font-weight: 700; font-size: 20px;
    line-height: 1;
  }
  .title {
    position: absolute; left: 40px; top: 158px; width: 480px;
    text-transform: uppercase; line-height: 1;
  }
  .title-line1 {
    display: block; color: var(--crimson); font-weight: 700;
    font-size: 78px; letter-spacing: 1px;
  }
  .title-line2 {
    display: block; color: var(--ink); font-weight: 700;
    font-size: 44px; margin-top: 8px; white-space: nowrap;
  }
  .title-line2 .light { font-weight: 400; }
  .class-pill {
    position: absolute; left: 42px; top: 299px; width: 476px; height: 34px;
    display: flex; border-radius: 9px; overflow: hidden;
    font-weight: 600; font-size: 17px; color: var(--white);
    text-transform: uppercase;
  }
  .class-pill .label {
    background: var(--crimson); width: 244px;
    display: flex; align-items: center; justify-content: center;
  }
  .class-pill .time {
    background: var(--gold); flex: 1; border-radius: 9px;
    display: flex; align-items: center; justify-content: center;
    margin-left: -4px;
  }
  .class-pill .time .light { font-weight: 400; margin: 0 5px; }
  .worship {
    position: absolute; left: 45px; top: 343px;
    font-size: 31px; font-weight: 500; color: var(--ink);
  }
  .worship .hour { color: var(--crimson); font-weight: 700; }
  .address {
    position: absolute; left: 40px; top: 396px; width: 462px; height: 50px;
    background: var(--crimson); border-radius: 9px 9px 0 0;
    display: flex; align-items: center; gap: 8px; padding-left: 10px;
    color: var(--white); font-weight: 600; font-size: 19px;
  }
  .address svg { width: 16px; height: 20px; flex: none; }
  .footer-band {
    position: absolute; left: 0; bottom: 0; width: 100%; height: 100%;
  }
  .website {
    position: absolute; left: 44px; top: 463px;
    color: var(--white); font-size: 22px; letter-spacing: 1.2px;
  }
  .website strong { font-weight: 700; }
  .visual {
    position: absolute; left: 0; top: 0; width: 1073px; height: 536px;
  }
</style>
</head>
<body>
  <main class="sign">
    <svg class="visual footer-band" viewBox="0 0 1073 536" aria-hidden="true">
      <defs>
        <linearGradient id="panelRed" x1="0" y1="0" x2="0" y2="1">
          <stop offset="0" stop-color="#c0193d"/>
          <stop offset="1" stop-color="#a50f2b"/>
        </linearGradient>
      </defs>
      <polygon points="0,445 502,445 561,536 0,536" fill="var(--black)"/>
      <rect x="576" y="0" width="497" height="536" fill="url(#panelRed)"/>
      <polygon points="576,497 1073,492 1073,536 576,536" fill="var(--white)"/>
      <polygon points="576,505 1073,500 1073,529 576,529" fill="var(--gold)"/>
      <rect x="576" y="529" width="497" height="7" fill="var(--black)"/>
    </svg>

    <svg class="visual" viewBox="0 0 1073 536" role="img" aria-label="Open arched wooden church doors revealing a sanctuary with an altar and pews">
      <defs>
        <linearGradient id="doorScene" x1="0" y1="0" x2="1" y2="0">
          <stop offset="0" stop-color="#7a4a3a"/>
          <stop offset="0.25" stop-color="#9a6a52"/>
          <stop offset="0.5" stop-color="#e6dcc8"/>
          <stop offset="0.75" stop-color="#9a6a52"/>
          <stop offset="1" stop-color="#7a4a3a"/>
        </linearGradient>
      </defs>
      <path d="M576,120 L655,120 Q690,120 700,105 Q740,70 820,68 Q900,70 940,105 Q955,120 975,118 L1073,118 L1073,492 L576,497 Z"
            fill="url(#doorScene)" stroke="var(--white)" stroke-width="5"/>
    </svg>

    <div class="brand">
      <span class="brand-mark"></span>
      <span class="brand-name">Ferndale Chapel of Grace</span>
    </div>

    <h1 class="title">
      <span class="title-line1">Ferndale</span>
      <span class="title-line2">Chapel <span class="light">of</span> Grace</span>
    </h1>

    <div class="class-pill">
      <span class="label">Discipleship Classes</span>
      <span class="time">Sundays<span class="light">at</span>9:00am</span>
    </div>

    <p class="worship">Sunday Worship at <span class="hour">10:30am</span></p>

    <div class="address">
      <svg viewBox="0 0 16 20" aria-hidden="true">
        <path d="M8 0C3.6 0 0 3.4 0 7.7 0 13 8 20 8 20s8-7 8-12.3C16 3.4 12.4 0 8 0z" fill="var(--gold)"/>
        <circle cx="8" cy="7.5" r="3" fill="var(--crimson)"/>
      </svg>
      <span>48 Willow Creek Road, Ferndale, PA 16620</span>
    </div>

    <p class="website">www.<strong>ferndalechapelofgrace</strong>.com</p>
  </main>
</body>
</html>
```